Veltora Software Business Card Design

We are a new organization called Veltora. We are a software as a service provider. We deliver a project and program management solution via the internet, so everyone has the ability to work together and collaborate. Its an enterprise platform and we will focus on 50 plus employee company.

We have a website in place
www.veltora-demo.com

Use this as a start of producing the business card. The logo is there as well, but if you have a great and better solution...

Color scheme's could be inline with the website, but don't pin point on it. We can always change the website, logo, color scheme etc.

Target Market(s)

B2B, Projectmembers, projectmanagers, ICT, CTO, Marketing Managers

Industry/Entity Type

Software

Requirements
Must have
• Marten Kuyvelsma

Tel: +31 255 47 09 36
Mob: +31 6 927 15 062
marten@veltora-demo.com
Oostelingpad 84c
2184 KT Nieuw Vennep

Www.veltora-demo.com
social media links

```html
<!DOCTYPE html>
<html lang="en">
<head>
<meta charset="utf-8">
<title>Veltora business card</title>
<link href="https://fonts.googleapis.com/css2?family=Lato:wght@300;400&display=swap" rel="stylesheet">
<style>
  :root {
    --backdrop: #2b2b2d;
    --lime: #9ccc2c;
    --lime-light: #b6dc52;
    --lime-deep: #8cc21e;
    --paper: #ffffff;
    --ink: #1f1f1f;
    --ink-soft: #3a3a3a;
    --social: #8a8f96;
  }
  * { margin: 0; padding: 0; box-sizing: border-box; }
  html, body { width: 1200px; height: 700px; overflow: hidden; }
  body {
    background: var(--backdrop);
    font-family: "Lato", Arial, sans-serif;
    position: relative;
  }
  .card {
    position: absolute;
    top: 190px;
    width: 520px;
    height: 320px;
    border-radius: 3px;
    box-shadow: 0 14px 30px rgba(0,0,0,.45);
    overflow: hidden;
  }
  .card--front { left: 50px; }
  .card--back { left: 630px; background: var(--paper); }

  .front-texture {
    position: absolute; inset: 0;
    background: radial-gradient(ellipse at 70% 60%, var(--lime-light), var(--lime) 55%, var(--lime-deep));
  }
  .front-logo {
    position: absolute;
    left: 150px; top: 92px;
    font-weight: 300;
    font-size: 74px;
    letter-spacing: 1px;
    color: var(--paper);
  }
  .front-url {
    position: absolute;
    left: 150px; top: 212px;
    font-weight: 400;
    font-size: 12px;
    color: var(--paper);
  }

  .back-logo {
    position: absolute;
    left: 40px; top: 30px;
    font-weight: 300;
    font-size: 54px;
    color: var(--lime);
  }
  .holder-name {
    position: absolute;
    left: 40px; top: 118px;
    font-size: 16px;
    color: var(--ink);
  }
  .contact-list {
    position: absolute;
    left: 40px; top: 148px;
    list-style: none;
    font-size: 12px;
    line-height: 16px;
    color: var(--ink-soft);
  }
  .contact-list .label {
    display: inline-block;
    width: 14px;
    color: var(--lime);
    font-weight: 400;
  }
  .address {
    position: absolute;
    left: 40px; top: 208px;
    font-size: 12px;
    color: var(--ink-soft);
  }
  .social-links {
    position: absolute;
    right: 30px; bottom: 26px;
    display: flex;
    gap: 6px;
  }
  .social-links span {
    width: 20px; height: 20px;
    border-radius: 3px;
    background: var(--social);
  }
</style>
</head>
<body>
  <section class="card card--front">
    <div class="front-texture" role="img" aria-label="Lime green background with a faint honeycomb pattern"></div>
    <div class="front-logo">Veltora</div>
    <div class="front-url">www.veltora-demo.com</div>
  </section>

  <section class="card card--back">
    <div class="back-logo">Veltora</div>
    <div class="holder-name">Marten Kuyvelsma</div>
    <ul class="contact-list">
      <li><span class="label">m</span>+31 255 47 09 36</li>
      <li><span class="label">p</span>+31 6 927 15 062</li>
      <li><span class="label">e</span>marten@veltora-demo.com</li>
    </ul>
    <div class="address">Oostelingpad 84c, 2184 KT Nieuw Vennep</div>
    <div class="social-links" role="img" aria-label="Social media links">
      <span></span><span></span><span></span><span></span>
    </div>
  </section>
</body>
</html>
```